Web Design for Solar Energy Consultancy Company

~ May 3, 2017 Update ~
As our project is rapidly progressing towards its completion, we started building up the list of designs that attracted the most of the team's attention. Additional submittals are still most welcome. Before submitting your proposal, however, we can recommend to review the concepts that received 4 stars as these are the ones that, in our opinion, most closely match the brief's requirements. Thank you!!
~ April 30, 2017 Update ~
The project deadline has been extended to attract a broader design community and to better tailor the final design to the requirements of the project.
A "light", "clean" (minimalistic), professionally looking, unique design is expected. Please, try to avoid industry cliches. Also, please use green, which became another industry cliche, with great caution. The brief provides minimum details to foster creativity. With the same notion in mind, the page content information is not provided.
Thank you for your feedback and support of the project!!
~ April 22, 2017 Update ~
Additional comments after starting receiving more designs:
- your attention to the brief's requirements will be highly appreciated. It is expected that the design is unique - standard, commonly used, images, formats and approaches do not fall under this category. There is no need to "bombard" with slightly different variations of the same design. It is expected that a conceptual (preliminary) design is submitted first, and, after it is reviewed (each design will receive a star rating and, if the star rating is greater than 3, a detailed feedback), the requested changes are implemented. We believe this will allow to approach the design process more efficiently and safe additional time to both the Designers's Community and our company. Thank you for understanding.
Clarification, please submit two variations of a design:
1) 1 page "business card" design that the company will be able to use during its startup stage;
2) the fully functional design (as per the requirements outlined below) for the company to transition to after the start-up period is over. Same design principles as developed for option 1 should be used for this variation.
Additional clarification, please note that the news block will not require images (at least during the start-up stage). It is envisioned to be a news feeder.
~ April 21, 2017 Update ~
Preliminary comments after receiving first designs:
- please try to create a unique design, using common elements wisely. Though such solar energy "attributes" as a solar panel or a bulb are very well recognized and allow quickly identify the nature of the business, they also became so common that in many cases a design may seem very similar to the one of others (Oh!, I've already seen this... effect).
- please try to introduce the company's logo unobtrusively. The size and position of the logo should clearly identify the company, but the message should be subtle, the logo should not distract from the main design. Brask's swoosh did not need to occupy have the screen.
- please use the green color with caution as it was with the company's logo. True, it is a green energy. But there is no need for the color to "scream" about it. Use the amount of green and its tone (avoid acid green) wisely.
--------------------------------------------------------------------------------
1. Main Goal
Develop a website that can represent the company to the industry stakeholders and become its "business card" during the start-up stage.
2. Secondary Goal
Develop a structure of a fully functional website that the "business card" design can eventually be transformed to staying consistent with the original design principles.
3. Key Audience
Varolu Corp. is providing consulting and technical services in the area of Solar Energy. The industry stakeholders include project developers, financial community, governmental bodies, OEMs, and competition.
4. Site Map
- HOME
• About
• Services
• Solar Energy
• News
• Contacts
• Social Media
- SERVICES*
- PROJECTS*
- FINANCE*
- TRAINING*
- SOLAR (ENERGY)*
* Maybe inactive / partially functional during the start-up stage.
5. Technical Specifications
Online brochure website during the start-up stage with a capability to be eventually transformed to a fully functional website while preserving the original design principles.
The design to be appealing, "light", professional, and with an intuitive and easy to navigate interface. Modern coding principles supporting efficiency and security to be utilized. Newest industry trends in website coding will be welcome.
The website to be designed so that it would fit well a computer, tablet, or mobile phone screen of any size. Cross-platform functionality to be taken into consideration to ensure that the website is fully functional on any platform.
Company's logo has already been designed and will be shared with the short-listed designers during the final design stage.
6. Interaction
The website will provide information about the company, our services, and projects. In addition, the industry insight, accumulated knowledge, and most recent trends are planned to be shared with stakeholders and attract and retain the audience.
Interaction with designers during the website development is envisioned to go through the following steps:
a) conceptual design - to be proposed by a designer originally. All conceptual designs will be reviewed and a feedback provided to pre-selected designers;
b) (preliminary and) final design - depending on the level of additional changes required can be broken into two steps. After discussing preliminary designs, company images will be provided to the selected finalists, who will compete with their final proposals.
7. Industry Stakeholders
- https://www.quellbrin.com/power/solar-power.- http://www.pakortavon.com/
- http://www.vellitrazo.com/about/company/
- https://www.oruxem.com/energy/index.html
8. Budget
Defined by the project.
9. Timescale
Defined by the project.
12. Additional Info
- No copy-cats, standard graphics, or cliches please!
- Additional information / clarifications will be gladly provided upon request.
- This specification may be updated throughout the project to reflect discussions with / changes proposed by the Designers community.

```html
<!DOCTYPE html>
<html lang="en">
<head>
<meta charset="utf-8">
<title>Varolu Corp. — Energy of the Future</title>
<link href="https://fonts.googleapis.com/css2?family=Montserrat:wght@400;500;600;700&family=Open+Sans:wght@400;600;700&family=Roboto:wght@500;700&display=swap" rel="stylesheet">
<style>
:root{
  --orange:#f7a81b;
  --ink:#2e2e2e;
  --text:#555;
  --muted:#8a8a8a;
  --line:#cfcfcf;
  --band:#ececec;
  --white:#fff;
}
*{margin:0;padding:0;box-sizing:border-box}
html,body{width:1200px;height:2372px;overflow:hidden;background:var(--white)}
body{position:relative;font-family:"Open Sans",sans-serif;color:var(--text)}
.abs{position:absolute}

/* header */
.site-header{position:absolute;left:0;top:0;width:1200px;height:80px;background:var(--white)}
.brand{position:absolute;left:100px;top:20px;display:flex;align-items:center;gap:12px}
.brand-dot{width:40px;height:40px;border-radius:50%;background:var(--orange)}
.brand-name{font-family:"Montserrat",sans-serif;font-weight:600;font-size:30px;letter-spacing:1px;color:var(--ink)}
.contact{position:absolute;top:15px;display:flex;align-items:center;gap:9px;font-size:13px;color:var(--ink)}
.contact svg{display:block}
.contact-mail{left:833px}
.contact-phone{left:992px}
.main-nav{position:absolute;top:54px;left:478px;display:flex;font-family:"Montserrat",sans-serif;font-size:12.5px;font-weight:500;color:var(--ink);letter-spacing:.5px}
.main-nav span{position:absolute;white-space:nowrap}

/* hero */
.hero{position:absolute;left:0;top:80px;width:1200px;height:495px;
  background:linear-gradient(180deg,#4c5560 0%,#6a5a57 35%,#3b4452 60%,#2c3646 80%,#6d6257 100%)}
.hero-title{position:absolute;left:0;top:320px;width:1200px;text-align:center;font-family:"Montserrat",sans-serif;font-weight:700;font-size:44px;color:var(--white);letter-spacing:1px}
.hero-rule{position:absolute;left:0;top:575px;width:1200px;height:7px;background:var(--orange)}

/* section heads */
.section-title{position:absolute;left:0;width:1200px;text-align:center;font-family:"Roboto",sans-serif;font-weight:700;font-size:26px;color:var(--ink);letter-spacing:.5px}
.section-title em{font-style:normal;color:var(--orange)}
.lead{position:absolute;text-align:center;font-size:11.5px;line-height:22px;color:var(--muted)}

/* feature cards */
.feature-card{position:absolute;top:806px;width:308px;height:328px;background:var(--white);box-shadow:0 2px 12px rgba(0,0,0,.13);text-align:center}
.feature-icon{position:absolute;left:124px;top:50px}
.feature-title{position:absolute;left:0;top:110px;width:100%;font-family:"Montserrat",sans-serif;font-weight:600;font-size:16.5px;color:var(--ink);letter-spacing:.5px}
.feature-rule{position:absolute;left:138px;top:144px;width:32px;height:2px;background:var(--ink)}
.feature-text{position:absolute;left:38px;top:166px;width:232px;font-size:11.5px;line-height:21px;color:#9a9a9a}
.btn{position:absolute;left:92px;top:248px;width:121px;height:38px;background:var(--orange);font-family:"Montserrat",sans-serif;font-weight:600;font-size:12.5px;line-height:38px;color:var(--ink);letter-spacing:.5px}

/* offer */
.offer-band{position:absolute;left:0;top:1203px;width:1200px;height:219px;
  background:linear-gradient(180deg,#4a5058 0%,#2f353d 55%,#1f242b 100%)}
.offer-title{position:absolute;left:0;top:1230px;width:1200px;text-align:center;font-family:"Montserrat",sans-serif;font-weight:600;font-size:29px;color:var(--white);letter-spacing:1px}
.offer-lead{position:absolute;left:120px;top:1280px;width:960px;text-align:center;font-size:12.5px;line-height:22px;font-weight:600;color:var(--white)}
.offer-box{position:absolute;top:1513px;width:300px;height:209px;border:1px solid #bdbdbd;background:var(--white);text-align:center}
.offer-photo{position:absolute;top:1345px;width:283px;height:182px}
.offer-box h3{position:absolute;left:0;top:40px;width:100%;font-family:"Montserrat",sans-serif;font-weight:600;font-size:15px;color:var(--ink);letter-spacing:.4px}
.offer-box p{position:absolute;left:14px;top:76px;width:272px;font-size:11px;line-height:21px;color:#8a8a8a;text-align:justify;text-align-last:center}
.read-more{position:absolute;left:0;top:174px;width:100%;font-size:12px;color:var(--ink)}
.read-more span{border-bottom:1px solid var(--ink)}

/* testimonials */
.client-photo{position:absolute;top:1888px;width:276px;height:259px}
.client-name{position:absolute;left:0;top:160px;width:100%;text-align:center;font-family:"Montserrat",sans-serif;font-weight:600;font-size:24px;color:var(--white);letter-spacing:2px}
.client-social{position:absolute;left:0;top:210px;width:100%;display:flex;justify-content:center;gap:22px}
.client-social i{width:14px;height:14px;border-radius:50%;background:var(--white)}

/* partners */
.partners{position:absolute;left:0;top:2195px;width:1200px;height:127px;background:var(--band)}
.partner{position:absolute;top:48px;font-family:"Open Sans",sans-serif;font-size:25px;font-weight:600;color:#5d6b77}
.partner-shape{position:absolute;top:32px;left:522px;width:198px;height:58px;background:#b7dcec}

/* footer */
.site-footer{position:absolute;left:0;top:2322px;width:1200px;height:50px;background:var(--orange);text-align:center;font-family:"Montserrat",sans-serif;font-weight:600;font-size:13px;line-height:50px;color:var(--ink);letter-spacing:1.5px}
</style>
</head>
<body>

<header class="site-header">
  <div class="brand"><span class="brand-dot"></span><span class="brand-name">VAROLU</span></div>
  <div class="contact contact-mail">
    <svg width="14" height="11" viewBox="0 0 14 11"><rect width="14" height="11" rx="1" fill="#f7a81b"/><path d="M1 1.5 7 6l6-4.5" stroke="#fff" stroke-width="1.3" fill="none"/></svg>
    <span>info@ varolu.com</span>
  </div>
  <div class="contact contact-phone">
    <svg width="13" height="13" viewBox="0 0 13 13"><rect width="13" height="13" rx="2" fill="#f7a81b"/><path d="M4 3c0 3 2.5 6 6 6.5l.5-1.5-1.8-.8-.8.8C6.7 7.3 5.9 6.5 5.5 5.3l.8-.8-.8-1.8z" fill="#fff"/></svg>
    <span>+41 5530 218</span>
  </div>
  <nav class="main-nav">
    <span style="left:0">HOME &#9662;</span>
    <span style="left:105px">SERVICES</span>
    <span style="left:222px">PROJECTS</span>
    <span style="left:345px">FINANCE</span>
    <span style="left:460px">TRAINING</span>
    <span style="left:578px">SOLAR</span>
  </nav>
</header>

<section class="hero" role="img" aria-label="Wind turbines standing behind rows of solar panels under a dusky sky"></section>
<h1 class="hero-title">ENERGY OF THE FUTURE</h1>
<div class="hero-rule"></div>

<h2 class="section-title" style="top:624px">ONE-STOP <em>SOLAR POWER</em> SOLUTIONS</h2>
<p class="lead" style="left:132px;top:683px;width:936px">Lorem ipsum is simply dummy text of the printing and typesetting industry. Lorem Ipsum has been the industry's standard dummy text ever since the 1500s, when an unknown printer took a galley of type and scrambled it to make a type specimen book. It has survived not only five centuries,Lorem Ipsum is simply dummy text of the printing and typesetting industry. Lorem Ipsum has been the industry's standard dummy text ever since the 1500s, when an unknown printer took a galley of type and scrambled it to make a type specimen book. It has survived not only five centuries,</p>

<article class="feature-card" style="left:112px">
  <svg class="feature-icon" width="60" height="48" viewBox="0 0 60 48" fill="none" stroke="#555" stroke-width="1.5"><path d="M6 20h38l-5 22H1z"/><path d="M4 27h37M2.5 35h37M16 20l-4 22M29 20l-3 22"/><circle cx="48" cy="10" r="5"/><path d="M48 1v3M48 16v3M57 10h-3M42 10h-3M54 4l-2 2M44 14l-2 2M54 16l-2-2"/></svg>
  <h3 class="feature-title">RENEWABLE ENERGY</h3>
  <div class="feature-rule"></div>
  <p class="feature-text">Lorem ipsum dolor sit amet, consectetur adipiscing elit. Morbi tincidunt commodo mi. Pellentesque vitae bibendum urna. Mauris at</p>
  <div class="btn">READ MORE</div>
</article>
<article class="feature-card" style="left:444px">
  <svg class="feature-icon" width="60" height="44" viewBox="0 0 60 44" fill="none" stroke="#555" stroke-width="1.5"><circle cx="20" cy="18" r="8"/><path d="M17 26v6h6v-6M20 3v3M7 18H4M36 18h-3M10 8l2 2M30 8l-2 2"/><path d="M23 32c4 6 14 6 16-2v-8M36 22h8v8h-8M44 24h5M44 28h5"/></svg>
  <h3 class="feature-title" style="top:104px">DIVERSE APPLICATIONS</h3>
  <div class="feature-rule"></div>
  <p class="feature-text">Maecenas maximus feugiat massa sed pharetra. Suspendisse ut sem ut justo condimentum congue at nec ex. Praesent lacinia imperdiet</p>
  <div class="btn">READ MORE</div>
</article>
<article class="feature-card" style="left:777px">
  <svg class="feature-icon" width="60" height="44" viewBox="0 0 60 44" fill="none" stroke="#555" stroke-width="1.5"><circle cx="30" cy="22" r="12"/><ellipse cx="30" cy="22" rx="26" ry="7" transform="rotate(-18 30 22)"/></svg>
  <h3 class="feature-title">SOLAR IS CARBON-FREE</h3>
  <div class="feature-rule"></div>
  <p class="feature-text">Ut turpis lacus, auctor sit amet metus eget, lacinia fringilla magna. Aliquam quis malesuada ipsum. Donec efficitur tincidunt egestas. Nullam</p>
  <div class="btn">READ MORE</div>
</article>

<section class="offer-band" role="img" aria-label="Solar panel field with cooling towers and a tree in the background"></section>
<h2 class="offer-title">WHAT WE OFFER</h2>
<p class="offer-lead">Lorem Ipsum is simply dummy text of the printing and typesetting industry. Lorem Ipsum has been the industry's standard dummy text ever since the 1500s, when an unknown printer took a galley of type and scrambled it to make a type specimen book. centuries</p>

<div class="offer-box" style="left:108px">
  <h3>OWNER'S &amp; LENDER'S ENGINEER</h3>
  <p>Lorem Ipsum is simply dummy text of the printing and typesetting industry. Lorem Ipsum has been the industry's standard dummy text ever since the 1500s, when an unknown printer</p>
  <div class="read-more"><span>continue reading &#10230;</span></div>
</div>
<div class="offer-box" style="left:433px">
  <h3>DETAILED PROJECT REPORT</h3>
  <p>Lorem Ipsum is simply dummy text of the printing and typesetting industry. Lorem Ipsum has been the industry's standard dummy text ever since the 1500s, when an unknown printer</p>
  <div class="read-more"><span>continue reading &#10230;</span></div>
</div>
<div class="offer-box" style="left:760px">
  <h3>APPLICATION FACILITATION</h3>
  <p>Lorem Ipsum is simply dummy text of the printing and typesetting industry. Lorem Ipsum has been the industry's standard dummy text ever since the 1500s, when an unknown printer</p>
  <div class="read-more"><span>continue reading &#10230;</span></div>
</div>
<div class="offer-photo" style="left:117px;background:linear-gradient(180deg,#e0751c 0%,#f3a12a 45%,#2a3142 70%,#1a1f2a 100%)" role="img" aria-label="Wind turbines and solar panels against an orange sunset"></div>
<div class="offer-photo" style="left:443px;background:linear-gradient(180deg,#b9b6dc 0%,#f5dcc0 30%,#e58a66 60%,#9a4f52 100%)" role="img" aria-label="Close view of a solar panel glowing in bright sunlight"></div>
<div class="offer-photo" style="left:768px;background:linear-gradient(180deg,#3a8ed4 0%,#8fc2ea 45%,#c9d7e4 70%,#6f8aa6 100%)" role="img" aria-label="Technician in orange workwear installing a solar panel under a blue sky"></div>

<h2 class="section-title" style="top:1774px">WHAT <em>CLIENT SAY'S</em> ABOUT US</h2>
<p class="lead" style="left:268px;top:1820px;width:664px">Lorem Ipsum is simply dummy text of the printing and typesetting industry. Lorem Ipsum has been the industry's standard dummy text ever since the 1500s, when an unknown printer</p>

<div class="client-photo" style="left:147px;background:linear-gradient(180deg,#b9b9b4 0%,#9d9f9a 60%,#3fb3c4 100%)" role="img" aria-label="Portrait of a smiling client with short blonde hair and glasses"></div>
<div class="client-photo" style="left:457px;background:linear-gradient(180deg,#f2bc4a 0%,#e9ad35 100%)" role="img" aria-label="Portrait of a smiling client with an orange overlay">
  <div class="client-name">MARLA QUINT</div>
  <div class="client-social"><i></i><i></i><i></i></div>
</div>
<div class="client-photo" style="left:778px;background:linear-gradient(180deg,#d8d6d3 0%,#b9b6b2 65%,#5f8fbf 100%)" role="img" aria-label="Portrait of a smiling bearded client in a blue shirt"></div>

<section class="partners">
  <span class="partner" style="left:122px;color:#3a7a4a">Pakortavon Energy</span>
  <div class="partner-shape"></div>
  <span class="partner" style="left:842px;color:#6a6a6a;font-weight:400"><span style="display:inline-block;width:24px;height:24px;border-radius:50%;background:var(--orange);vertical-align:-4px;margin-right:10px"></span>Vellitrazo</span>
</section>

<footer class="site-footer">&copy; 2017 VAROLU. ALL RIGHTS RESERVED</footer>

</body>
</html>
```